Bold Cover needed for a book on Workplace Bullying

I need a book cover design for a book titled, “Iron Silence?” The book recounts my story of bullying in the workplace. It also includes chapters on how readers can minimize/stop workplace bullying, write an effective complaint, and ensure their own mental wellbeing.
I am looking for a bold design using red and black, and possibly distressed lettering. The covers of other books dealing with this subject do not reflect my vision. They are often too childish or look too academic. This book needs to stress the serious nature of a toxic workplace, while appealing to readers experiencing a similar situation. I’d like the cover to reflect the mental anguish associated with workplace bullying (hence the distressed lettering).
I have included a cover that appeals to me (although the coloring is wrong). That said, I am also very happy (and excited) to see your creative input!
On the cover, it should have the following:
Title: Iron Silence?
Subtitle: How the Harbour Works Department Condones Bullying & Ruins Lives
Author: Owen Frick
Other relevant details:
Book size: 5.5” x 8.5”
Back cover will have a blurb, author picture/short bio, and barcode
The blurb on the back cover reads:
Undermining, intimidation and threats
Despite the Department of Harbour Works allegedly holding a zero tolerance for bullying, these behaviours were an everyday occurrence in at least one workplace. Even after a decade of complaints, numerous witnesses and physical proof, the department failed to act. Instead, they looked the other way, allowing one powerful and well-connected individual to end careers and ruin lives.
After being targeted, one teacher resolved to put an end to the abuse experienced by more than fifty employees. His startling story reveals the relentless bullying, mental health ramifications, and insidious tactics used to cover up the corrosive behaviour.
Those who have experienced a toxic workplace will also find much needed support and guidance, intended to minimise suffering and detail a clear way forward. Chapters include dealing with bullying in the workplace, how to lodge a successful complaint, and how to stay sane during any potential legal action.

```html
<!DOCTYPE html>
<html lang="en">
<head>
<meta charset="utf-8">
<title>Iron Silence? — Book Cover</title>
<link rel="stylesheet" href="https://fonts.googleapis.com/css2?family=Anton&family=Open+Sans:wght@400;700&display=swap">
<style>
  :root {
    --page-bg: #ece6dc;
    --back-black: #0a0a0d;
    --cover-red: #ec1c24;
    --spine-red: #e11b22;
    --ink-black: #111111;
    --paper-white: #ffffff;
    --paper-grey: #e4e4e4;
    --photo-grey: #5a5a5a;
  }
  html, body {
    margin: 0;
    padding: 0;
    width: 1200px;
    height: 963px;
    overflow: hidden;
    background: var(--page-bg);
  }
  .canvas {
    position: relative;
    width: 1200px;
    height: 963px;
  }
  .back-cover {
    position: absolute;
    left: 53px; top: 47px;
    width: 506px; height: 784px;
    background: var(--back-black);
  }
  .blurb {
    position: absolute;
    left: 116px; top: 154px;
    width: 374px;
    font-family: "Open Sans", sans-serif;
    font-size: 14px;
    line-height: 16.9px;
    color: var(--paper-white);
    text-align: justify;
  }
  .blurb p { margin: 0 0 16.9px; }
  .author-photo {
    float: left;
    width: 118px; height: 102px;
    margin: 2px 20px 4px 4px;
    background: var(--photo-grey);
  }
  .spine {
    position: absolute;
    left: 559px; top: 47px;
    width: 84px; height: 784px;
    background: var(--spine-red);
  }
  .spine-title, .spine-author {
    position: absolute;
    white-space: nowrap;
    transform-origin: left top;
    transform: rotate(-90deg);
    color: var(--ink-black);
  }
  .spine-title {
    left: 575px; top: 476px;
    font-family: "Anton", sans-serif;
    font-size: 44px;
    line-height: 44px;
  }
  .spine-author {
    left: 588px; top: 778px;
    font-family: "Open Sans", sans-serif;
    font-weight: 700;
    font-size: 19px;
    line-height: 22px;
  }
  .front-cover {
    position: absolute;
    left: 643px; top: 47px;
    width: 508px; height: 784px;
    background: linear-gradient(90deg, #d8181f 0, var(--cover-red) 40px, var(--cover-red) 100%);
  }
  .title-art {
    position: absolute;
    left: 643px; top: 150px;
  }
  .torn-band {
    position: absolute;
    left: 643px; top: 512px;
  }
  .subtitle {
    position: absolute;
    left: 643px; top: 562px;
    width: 508px;
    margin: 0;
    text-align: center;
    font-family: "Anton", sans-serif;
    font-weight: 400;
    font-size: 31px;
    line-height: 32px;
    letter-spacing: -0.6px;
    color: var(--cover-red);
  }
  .subtitle .emphasis { color: var(--ink-black); }
  .front-author {
    position: absolute;
    left: 643px; top: 762px;
    width: 508px;
    margin: 0;
    text-align: center;
    font-family: "Open Sans", sans-serif;
    font-weight: 700;
    font-size: 21px;
    line-height: 26px;
    color: var(--ink-black);
  }
</style>
</head>
<body>
<div class="canvas">

  <section class="back-cover"></section>
  <div class="blurb">
    <div class="author-photo" role="img" aria-label="Author photo placeholder"></div>
    <p>Lorem ipsum dolor sit amet, consectetur adipiscing elit. Pellentesque eu tortor eget dui mattis feugiat a pharetra felis. Aliquam eu sodales lacus. Sed id mollis turpis. Aliquam efficitur tempor ante, in lobortis lacus bibendum quis. Vivamus scelerisque sapien consequat mi tincidunt, at maximus ligula ultricies. Sed rutrum augue ligula, vel aliquam nisi laoreet nec. Cras tristique facilisis justo sed volutpat. Fusce in ex rutrum, mattis est nec, mattis libero. Nulla ac eleifend felis. Fusce rutrum, felis a sodales sagittis, sem ex porttitor erat, hendrerit efficitur dolor est a sapien.</p>
    <p>Pellentesque convallis ligula ut tortor accumsan, luctus maximus elit vestibulum. Pellentesque nunc turpis, tincidunt eget nunc eget, sollicitudin volutpat dolor. Curabitur sapien mi, auctor eget neque quis, suscipit sagittis ligula. Integer commodo tincidunt est scelerisque finibus.Curabitur augue dui, vestibulum tincidunt nulla vitae, dapibus luctus ex.</p>
    <p>Mauris blandit aliquet imperdiet. Etiam a est velit. Duis efficitur, ipsum vel pretium aliquam, ante felis scelerisque ante, et pretium turpis metus in nibh. Vivamus placerat felis sed eros lobortis,</p>
  </div>

  <section class="spine"></section>
  <div class="spine-title">IRON SILENCE?</div>
  <div class="spine-author">Owen Frick</div>

  <section class="front-cover"></section>

  <svg class="title-art" width="508" height="300" viewBox="0 0 508 300" aria-labelledby="cover-title">
    <title id="cover-title">Iron Silence?</title>
    <defs>
      <filter id="distress" x="0" y="0" width="100%" height="100%">
        <feTurbulence type="fractalNoise" baseFrequency="0.09" numOctaves="3" seed="4" result="noise"/>
        <feColorMatrix in="noise" type="matrix" values="0 0 0 0 0  0 0 0 0 0  0 0 0 0 0  14 0 0 0 -9.4" result="specks"/>
        <feComposite in="SourceGraphic" in2="specks" operator="out"/>
      </filter>
    </defs>
    <rect role="img" aria-label="Illustration of a giant hand pressing down on a seated office worker"
          x="140" y="36" width="96" height="64" fill="#d9d9d9"/>
    <text class="title-main" x="28" y="198" textLength="450" lengthAdjust="spacingAndGlyphs"
          font-family="Anton, sans-serif" font-size="250" fill="#111111" filter="url(#distress)">IRON</text>
    <text class="title-sub" x="27" y="289" textLength="459" lengthAdjust="spacingAndGlyphs"
          font-family="Anton, sans-serif" font-size="100" fill="#ffffff" filter="url(#distress)">SILENCE?</text>
  </svg>

  <svg class="torn-band" width="508" height="198" viewBox="0 0 508 198" aria-hidden="true">
    <defs>
      <linearGradient id="band-shade" x1="0" x2="1" y1="0" y2="0">
        <stop offset="0" stop-color="#e2e2e2"/>
        <stop offset="0.35" stop-color="#ffffff"/>
        <stop offset="1" stop-color="#ffffff"/>
      </linearGradient>
    </defs>
    <polygon fill="url(#band-shade)" points="
      0,20 14,17 22,19 35,14 48,18 60,13 72,17 85,15 96,9 108,15 120,12 133,16 146,10 158,14 170,11 184,15
      196,8 210,13 222,10 236,14 248,6 262,12 275,9 288,14 300,7 313,12 326,9 340,13 352,5 366,11 378,8 392,12
      404,6 418,11 430,8 444,12 456,5 470,10 482,7 496,10 508,4
      508,178 496,183 484,180 470,186 458,181 444,185 432,179 418,186 404,182 392,189 380,183 366,187 354,181
      340,188 328,184 314,190 300,184 288,189 274,185 262,191 248,186 236,190 222,185 210,192 196,187 184,191
      170,186 158,190 146,185 132,191 120,187 106,192 94,188 80,193 68,188 54,192 42,187 28,192 14,188 0,191"/>
  </svg>

  <h2 class="subtitle">How the Harbour Works<br>Department Condones <span class="emphasis">Bullying</span><br>&amp; Ruins Lives</h2>

  <p class="front-author">Owen Frick</p>

</div>
</body>
</html>
```